Business Card Design Project

I am community manager and social media strategist. I need a double sided business card with company logo and name. Looking for something professional, elegant but also a little bit original.

Industry/Entity Type

Business

Requirements
Must have
• - The logo and the colours are the company colours and a required to stay.
- The size should be: 84 x 55 mm (or 3.30 x 2.16)
- The file size should be: 1039 x 697 pixels (300 dpi)
- I'd like rounded corners. :)

Use the following contact information for the card:

Lucile Bravant
Stratégie médias sociaux / community management / édition de sites sociaux
mob. : 0687152930
lucile.bravant@maivox.fr
Twitter. : @lbravant
Skype : bravant.lucile

```html
<!DOCTYPE html>
<html lang="fr">
<head>
<meta charset="utf-8">
<title>Maivox – carte de visite</title>
<link rel="stylesheet" href="https://fonts.googleapis.com/css2?family=Barlow:wght@400;500;600&display=swap">
<style>
  :root {
    --brand-blue: #1468a6;
    --brand-blue-deep: #0c4f8b;
    --brand-blue-light: #2a86c6;
    --accent-cyan: #3fa3dc;
    --ink: #3a3a3a;
    --paper: #ffffff;
    --band: #eceef0;
    --pattern: #d6d9dc;
    --backdrop: #e6e8ea;
  }
  * { margin: 0; padding: 0; box-sizing: border-box; }
  html, body { width: 1200px; height: 900px; overflow: hidden; }
  body {
    background: var(--backdrop);
    font-family: "Barlow", Arial, sans-serif;
    position: relative;
  }
  .card {
    position: absolute;
    left: 300px;
    width: 600px;
    height: 393px;
    border-radius: 14px;
    overflow: hidden;
  }
  .card--front {
    top: 40px;
    background: linear-gradient(100deg, var(--brand-blue-light) 0%, var(--brand-blue) 45%, var(--brand-blue-deep) 100%);
  }
  .card--back {
    top: 467px;
    background: var(--paper);
  }
  .brand-lockup {
    position: absolute;
    display: flex;
    flex-direction: column;
    align-items: center;
    left: 0; right: 0;
    top: 62px;
  }
  .brand-lockup__dot {
    width: 100px; height: 100px;
    border-radius: 50%;
    background: var(--paper);
  }
  .brand-lockup__name {
    margin-top: 18px;
    font-weight: 600;
    font-size: 50px;
    letter-spacing: 2px;
    color: var(--paper);
  }
  .social-pattern {
    position: absolute;
    right: 0;
    bottom: 0;
  }
  .card--front .social-pattern {
    left: 70px; width: 400px; height: 60px;
    background: linear-gradient(90deg, rgba(255,255,255,0) 0%, rgba(255,255,255,0.28) 40%, rgba(255,255,255,0.12) 100%);
  }
  .back-band {
    position: absolute;
    left: 0; top: 0; right: 0;
    height: 105px;
    background: linear-gradient(180deg, #f6f7f8 0%, var(--band) 100%);
    display: flex;
    align-items: center;
    padding-left: 46px;
    gap: 12px;
  }
  .back-band__dot {
    width: 36px; height: 36px;
    border-radius: 50%;
    background: var(--brand-blue);
  }
  .back-band__name {
    font-weight: 600;
    font-size: 34px;
    letter-spacing: 1px;
    color: var(--brand-blue);
  }
  .contact {
    position: absolute;
    left: 44px;
    top: 148px;
    width: 520px;
    color: var(--ink);
  }
  .contact__name {
    font-size: 29px;
    font-weight: 500;
    color: var(--brand-blue);
    line-height: 1.1;
  }
  .contact__role {
    font-size: 17px;
    line-height: 1.35;
    margin-top: 4px;
    width: 470px;
  }
  .contact__list {
    margin-top: 26px;
    font-size: 18px;
    line-height: 1.3;
    display: grid;
    grid-template-columns: 88px auto;
    list-style: none;
  }
  .contact__list dt, .contact__list dd { margin: 0; }
  .contact__list .is-highlight { color: var(--accent-cyan); }
  .card--back .social-pattern {
    width: 270px; height: 110px;
    bottom: 12px;
    background: radial-gradient(ellipse at 60% 50%, var(--pattern) 0%, rgba(214,217,220,0.4) 55%, rgba(214,217,220,0) 80%);
  }
</style>
</head>
<body>
  <section class="card card--front" aria-label="Recto">
    <div class="brand-lockup">
      <div class="brand-lockup__dot"></div>
      <div class="brand-lockup__name">MAIVOX</div>
    </div>
    <div class="social-pattern" role="img" aria-label="Frise pâle de pictogrammes des réseaux sociaux (arobase, dièse, oiseau, bulles)"></div>
  </section>

  <section class="card card--back" aria-label="Verso">
    <header class="back-band">
      <div class="back-band__dot"></div>
      <div class="back-band__name">MAIVOX</div>
    </header>
    <div class="contact">
      <div class="contact__name">Lucile Bravant</div>
      <div class="contact__role">Stratégie médias sociaux / community management / édition de sites sociaux</div>
      <dl class="contact__list">
        <dt class="is-highlight">Email</dt><dd class="is-highlight">: lucile.bravant@maivox.fr</dd>
        <dt>Mobile</dt><dd>: 0687152930</dd>
        <dt>Twitter</dt><dd>: @lbravant</dd>
        <dt>Skype</dt><dd>: bravant.lucile</dd>
      </dl>
    </div>
    <div class="social-pattern" role="img" aria-label="Groupe pâle de pictogrammes des réseaux sociaux (arobase, dièse, oiseau, bulles)"></div>
  </section>
</body>
</html>
```